Migration Lawyers

Company: Thornbury & Co Lawyers & Migration Agents

Name: Gavin Rusholt BEc, LLB
Address: Level 19, 71 Pelham Street
Sydney, NSW, Australia 2000

Ph: +61 2 9357 2164
M: 0438261504
E: gavin@permit-nomadra.org.au
W: www.permit-nomadra.org.au

Target Market(s)

Migration Clients

Industry/Entity Type

It Company

Font styles to use
Script

Requirements
Must have
• Logo
Should not have
• Please scale the format to the printing size attached

```html
<!DOCTYPE html>
<html lang="en">
<head>
<meta charset="utf-8">
<title>Thornbury &amp; Co — Business Card</title>
<link rel="stylesheet" href="https://fonts.googleapis.com/css2?family=Parisienne&family=Tinos:wght@700&display=swap">
<style>
  :root {
    --backdrop: #e6e6e4;
    --card: #ffffff;
    --ink: #111111;
    --ink-soft: #2a2a2a;
    --ghost: #ececec;
    --rule: #9a9a9a;
    --shadow: rgba(0, 0, 0, 0.18);
  }
  * { margin: 0; padding: 0; box-sizing: border-box; }
  html, body {
    width: 1200px;
    height: 900px;
    overflow: hidden;
    background: var(--backdrop);
  }
  .canvas {
    position: relative;
    width: 1200px;
    height: 900px;
    display: flex;
    flex-direction: column;
    align-items: center;
    justify-content: center;
    gap: 60px;
  }
  .card {
    position: relative;
    width: 630px;
    height: 360px;
    background: var(--card);
    box-shadow: 0 6px 18px var(--shadow);
    overflow: hidden;
  }

  /* Contact side */
  .contact-side .ghost-name {
    position: absolute;
    top: 70px;
    right: 40px;
    font-family: "Tinos", serif;
    font-weight: 700;
    font-size: 46px;
    line-height: 1.05;
    color: var(--ghost);
    text-align: right;
  }
  .contact-side .ghost-name small {
    display: block;
    font-size: 22px;
  }
  .contact-details {
    position: absolute;
    left: 46px;
    top: 40px;
    font-family: "Parisienne", cursive;
    color: var(--ink-soft);
  }
  .person-name {
    font-size: 40px;
    line-height: 1;
    color: var(--ink);
  }
  .person-title {
    font-size: 22px;
    margin: 2px 0 0 12px;
  }
  .address {
    margin-top: 28px;
    font-size: 24px;
    line-height: 1.25;
  }
  .phones {
    margin-top: 20px;
    font-size: 24px;
    line-height: 1.25;
  }
  .web {
    margin-top: 16px;
    font-size: 21px;
    line-height: 1.3;
  }

  /* Brand side */
  .brand-side {
    display: flex;
    align-items: center;
    justify-content: center;
  }
  .brand {
    display: flex;
    align-items: center;
    gap: 22px;
  }
  .brand-circle {
    width: 140px;
    height: 96px;
    flex: none;
  }
  .brand-name {
    font-family: "Tinos", serif;
    font-weight: 700;
    color: var(--ink);
    line-height: 1.05;
  }
  .brand-name .firm {
    display: block;
    font-size: 44px;
  }
  .brand-name .tagline {
    display: block;
    font-size: 19px;
  }
</style>
</head>
<body>
<main class="canvas">

  <section class="card contact-side" aria-label="Business card, contact side">
    <p class="ghost-name" aria-hidden="true">Thornbury &amp; Co<small>Lawyers &amp; Migration Agents</small></p>
    <div class="contact-details">
      <h1 class="person-name">Gavin Rusholt</h1>
      <p class="person-title">BEc, LLB</p>
      <p class="address">Level 19, 71 Pelham Street<br>Sydney, NSW, Australia 2000</p>
      <p class="phones">Tel: +61 2 9357 2164<br>Mob: 0438261504</p>
      <p class="web">gavin@permit-nomadra.org.au<br>www.permit-nomadra.org.au</p>
    </div>
  </section>

  <section class="card brand-side" aria-label="Business card, brand side">
    <div class="brand">
      <svg class="brand-circle" viewBox="0 0 140 96" aria-hidden="true">
        <ellipse cx="70" cy="48" rx="67" ry="45" fill="none" stroke="var(--rule)" stroke-width="2"/>
      </svg>
      <p class="brand-name">
        <span class="firm">Thornbury &amp; Co</span>
        <span class="tagline">Lawyers &amp; Migration Agents</span>
      </p>
    </div>
  </section>

</main>
</body>
</html>
```